mosswickpartners Business Card Design

Business card with logo design for mosswickpartners. We are a group of professional project managers based on the Pareto Principle that 80% of the work is done by 20% of the people. I have a makeshift logo that uses a pi chart with 30% and 20% and the 20% pie slice is set slightly out and up. Have played around with a teal and orange colour scheme.

Industry/Entity Type

Business

Contact Information for Business Card

Harold Penbury
Director
mosswickpartners

0487 263019

```html
<!DOCTYPE html>
<html lang="en">
<head>
<meta charset="utf-8">
<title>mosswickpartners Business Card</title>
<link href="https://fonts.googleapis.com/css2?family=Open+Sans:wght@400;600&display=swap" rel="stylesheet">
<style>
  :root {
    --backdrop: #8a8a8a;
    --card: #f7f7f5;
    --orange: #e35d36;
    --teal: #1f8a93;
    --ink: #555a5c;
    --white: #ffffff;
    --value: #f2a27e;
  }
  * { margin: 0; padding: 0; box-sizing: border-box; }
  html, body {
    width: 1200px;
    height: 900px;
    overflow: hidden;
    background: var(--backdrop);
    font-family: "Open Sans", sans-serif;
  }
  .canvas {
    position: relative;
    width: 1200px;
    height: 900px;
  }
  .card {
    position: absolute;
    left: 300px;
    width: 600px;
    height: 366px;
    background: var(--card);
    overflow: hidden;
    box-shadow: 0 4px 14px rgba(0,0,0,0.18);
  }
  .card--brand { top: 64px; }
  .card--contact { top: 470px; }

  .brand {
    position: absolute;
    display: flex;
    align-items: center;
    gap: 12px;
    color: var(--orange);
    font-weight: 400;
  }
  .brand__dot {
    border-radius: 50%;
    background: var(--orange);
    flex: none;
  }
  .card--brand .brand {
    left: 50%;
    top: 50%;
    transform: translate(-50%, -50%);
    font-size: 40px;
  }
  .card--brand .brand__dot { width: 46px; height: 46px; }
  .card--contact .brand {
    left: 130px;
    top: 150px;
    transform: translate(-50%, -50%);
    font-size: 22px;
    gap: 8px;
  }
  .card--contact .brand__dot { width: 26px; height: 26px; }

  .panel {
    position: absolute;
    left: 260px;
    top: 0;
    width: 340px;
    height: 366px;
  }
  .panel__bg { position: absolute; inset: 0; }
  .panel__bg .orange { fill: var(--orange); }
  .panel__bg .teal { fill: var(--teal); }

  .holder {
    position: absolute;
    right: 30px;
    top: 58px;
    text-align: right;
  }
  .holder__name {
    color: var(--white);
    font-size: 24px;
    font-weight: 400;
    letter-spacing: 0.3px;
  }
  .holder__role {
    color: var(--ink);
    font-size: 12px;
  }
  .group {
    position: absolute;
    left: 80px;
    top: 146px;
    font-size: 15px;
    color: var(--teal);
  }
  .contact {
    position: absolute;
    left: 26px;
    top: 236px;
    list-style: none;
    font-size: 14px;
    line-height: 22px;
  }
  .contact__label { color: var(--white); }
  .contact__value { color: var(--value); }
</style>
</head>
<body>
<main class="canvas">
  <section class="card card--brand">
    <div class="brand"><span class="brand__dot"></span>mosswickpartners</div>
  </section>

  <section class="card card--contact">
    <div class="brand"><span class="brand__dot"></span>mosswickpartners</div>
    <div class="panel">
      <svg class="panel__bg" width="340" height="366" viewBox="0 0 340 366">
        <rect class="orange" x="0" y="0" width="340" height="366"/>
        <polygon class="teal" points="0,200 112,200 134,176 156,214 340,214 340,366 0,366"/>
      </svg>
      <div class="holder">
        <p class="holder__name">Harold Penbury</p>
        <p class="holder__role">Director</p>
      </div>
      <p class="group">mosswickpartners</p>
      <ul class="contact">
        <li><span class="contact__label">Phone:</span> <span class="contact__value">0487 263019</span></li>
        <li><span class="contact__label">Fax:</span> <span class="contact__value">0487 551204</span></li>
        <li><span class="contact__label">Adress:</span> <span class="contact__value">48 Calder Lane, Victoria 3921</span></li>
        <li><span class="contact__label">Email:</span> <span class="contact__value">hello@mosswickpartners.au</span></li>
      </ul>
    </div>
  </section>
</main>
</body>
</html>
```